Stitch Haven web site

I have been running an online business for 6 years.
www.stitchhaven.com.au I specialise in ribbons, buttons and unique craft materials. I sell online to individuals and shops with seperate retail and wholesale sites. The web page I'd like redesigned is my retail site.

It needs a clean, fresh look. I've recently had a new logo designed (thanks pixel guild!) and want the web site to incorporate the new design and colour scheme of black and white. (new logo attached as a file)

I no longer want the page with the large image www.stitchhaven.com.au I want to have the first page as the retail shop homepage.
http://www.stitchhaven.com.au/index.php so this page needs to have all the links

I want to the look to be fresh, modern and clear. It needs to be quick to load.

Notes from my IT guru: They need to know that the following tend to remain static with just the content section changing on each page; Header Left column (but different in the cart) right column (if required) footer
Updates

Thanks for your designs. 1/3 of my users use mobile devices so please take that into consideration. I would like the logo to be incorporated into the design and be a prominent feature (most have just used it as a tiny image in the top left corner. I would like it to be larger and more prominent.  thanks                                   

Thanks to all the designers who have submitted. Can you please add  'Boutique craft supplies' near the logo. That is my tag line. Thanks

Target Market(s)

Crafty females of all ages

Industry/Entity Type

Business

Requirements
Must have
• links to;
blog
gallery
chatterbook
snapboard
wholesale
space for an image which I change approx every 2 weeks
about Stitch Haven
contact
privacy policy
terms and conditions
newsletter sign up
shipping info
product search
Nice to have
• I am not sure if I want product images on the homepage? I have attached a few images.
Should not have
• not too much colour - I hate the green border I have now

```html
<!DOCTYPE html>
<html lang="en">
<head>
<meta charset="utf-8">
<title>Stitch Haven – Boutique craft supplies</title>
<link href="https://fonts.googleapis.com/css2?family=Arimo:ital,wght@0,400;0,700;1,400&display=swap" rel="stylesheet">
<style>
:root{
  --ink:#222;
  --text:#333;
  --muted:#888;
  --soft:#777;
  --topbar:#3b3b3b;
  --header:#efefef;
  --panel:#f1f1f1;
  --panel-head:#ebebeb;
  --line:#dedede;
  --white:#fff;
  --red:#e31b1b;
  --footer:#3a3a3a;
  --footer-text:#b5b5b5;
}
*{box-sizing:border-box;margin:0;padding:0}
html,body{width:888px;height:1200px;overflow:hidden;background:var(--white)}
body{position:relative;font-family:"Arimo",Arial,sans-serif;color:var(--text);font-size:11px}
.abs{position:absolute}

/* top bar */
.topbar{left:0;top:0;width:888px;height:30px;background:var(--topbar)}
.top-links{left:432px;top:0;height:30px;display:flex}
.top-links a{display:block;height:30px;line-height:30px;padding:0 20px;color:#cfcfcf;font-size:10px;text-decoration:none;border-left:1px solid #4d4d4d}
.top-links a:last-child{border-right:1px solid #4d4d4d}
.social-dot{top:3px;width:22px;height:22px;border-radius:50%;background:#8a8a8a;border:2px solid #5a5a5a}

/* header */
.header{left:0;top:30px;width:888px;height:78px;background:var(--header)}
.brand-tab{left:78px;top:0;width:132px;height:134px;background:linear-gradient(#e8e8e8,#cfcfcf);border-radius:0 0 60px 60px/0 0 22px 22px;box-shadow:0 3px 5px rgba(0,0,0,.35);display:flex;flex-direction:column;align-items:center;justify-content:center;gap:8px;z-index:3}
.brand-dot{width:30px;height:30px;border-radius:50%;background:var(--ink)}
.brand-name{font-size:17px;font-weight:700;color:var(--ink);letter-spacing:.2px}
.search{left:630px;top:10px;width:184px;height:24px;border-radius:6px;background:var(--white);display:flex;align-items:center;padding-left:8px;gap:7px;color:#c4c4c4;font-size:9px}
.main-nav{left:427px;top:48px;height:30px;display:flex;align-items:center}
.main-nav a{font-size:11px;color:#555;text-decoration:none;padding:0 10px;height:30px;line-height:30px}
.main-nav a.active{background:linear-gradient(#dedede,#c2c2c2);color:#333;padding:0 11px;margin-right:8px}

/* panels */
.panel{background:var(--panel)}
.panel-title{font-size:14px;font-weight:400;color:var(--ink);position:absolute;left:9px;top:14px}
.panel-link{position:absolute;right:12px;top:18px;font-size:9px;font-weight:700;color:var(--muted)}

.hero{left:80px;top:142px;width:513px;height:211px;background:var(--white);border:1px solid var(--line)}
.hero-image{left:6px;top:6px;width:499px;height:197px;background:linear-gradient(160deg,#cfe4ef 0%,#c7b4e6 30%,#e9b7cf 55%,#eee6a9 70%,#b9a2e0 88%,#e8e6ee 100%)}
.hero-arrow{top:88px}

.new-products{left:602px;top:142px;width:213px;height:206px}
.new-products .head{left:0;top:0;width:213px;height:40px;background:var(--panel-head)}
.cat-list{left:9px;top:50px;width:197px;list-style:none}
.cat-list li{font-size:11px;color:var(--muted);height:18px;line-height:18px;border-bottom:1px solid #e2e2e2}

.latest{left:80px;top:364px;width:513px;height:259px}
.card{width:89px;text-align:center}
.thumb{width:89px;height:54px}
.thumb.tape{background:linear-gradient(#e4eef2,#7fc8e3 50%,#d4e6ee)}
.thumb.ribbon{background:linear-gradient(#f5f5f5,#7a6f62 55%,#efefef)}
.thumb.tape-mono{background:linear-gradient(#f0f0f0,#bcbcbc 50%,#e6e6e6)}
.thumb.button{background:radial-gradient(circle at 40% 50%,#3a3a3a 0 30%,#e8e8e8 70%)}
.card .name{margin:5px -12px 0;font-size:10px;color:var(--text);white-space:nowrap}
.card .variant{font-size:7.5px;font-weight:700;color:var(--muted);margin-top:1px}
.card .price{font-size:10px;color:var(--muted);margin-top:1px}

.basket{left:602px;top:364px;width:213px;height:103px}
.basket-info{left:9px;top:50px;font-size:8.5px;font-weight:700;line-height:12px}
.basket-info .empty{color:var(--soft);margin-bottom:10px}
.basket-info .red{color:var(--red)}

.gallery{left:602px;top:478px;width:213px;height:145px}

.popular{left:80px;top:636px;width:513px;height:164px}
.deal{width:250px}
.deal .title{font-size:10.5px;color:var(--text);white-space:nowrap}
.deal .save{font-size:11px;color:var(--red);margin-top:1px}

.subscribe{left:602px;top:636px;width:213px;height:164px}
.sub-note{left:9px;top:53px;font-size:9px;font-weight:700;color:var(--soft)}
.sub-label{left:9px;top:82px;font-size:9px;font-weight:700;color:var(--soft)}
.sub-input{left:44px;top:76px;width:160px;height:22px;background:#d4d4d4}
.sub-btn{right:10px;top:114px;font-size:9px;font-weight:700;color:var(--ink)}

.sales-title{left:89px;top:812px;font-size:14px;font-weight:400;color:var(--ink)}

.join{left:602px;top:814px;width:213px;height:116px}
.social-name{font-size:14px;font-weight:700;color:#3d3d3d}

.blogs{left:80px;top:946px;width:513px;height:132px}
.quote-mark{font-size:28px;color:#666;font-family:Georgia,serif;line-height:1}
.quote-text{left:26px;top:60px;width:470px;font-size:10.5px;font-style:italic;color:var(--soft);line-height:15px}
.quote-by{right:25px;top:110px;font-size:9px;font-weight:700;color:var(--soft)}

.partners{left:602px;top:946px;width:213px;height:132px}
.badge{background:#5e4a46}

.postage{left:80px;top:1087px;width:735px;height:61px;background:var(--panel);border:1px solid var(--line)}
.postage-flag{left:8px;top:0}
.postage-text{left:0;top:10px;width:735px;text-align:center;font-size:8px;font-weight:700;color:var(--red);line-height:10px}

.footer{left:0;top:1174px;width:888px;height:26px;background:var(--footer);color:var(--footer-text);font-size:9px;line-height:26px}
.footer-links{left:80px;top:0;word-spacing:1px}
.footer-links span{margin:0 10px}
.footer-copy{right:73px;top:0}
</style>
</head>
<body>

<div class="abs topbar">
  <nav class="abs top-links">
    <a href="#">Stitch Haven Home</a>
    <a href="#">Shop Home</a>
    <a href="#">Basket</a>
  </nav>
  <span class="abs social-dot" style="left:731px" aria-hidden="true"></span>
  <span class="abs social-dot" style="left:760px" aria-hidden="true"></span>
  <span class="abs social-dot" style="left:789px" aria-hidden="true"></span>
</div>

<header class="abs header">
  <div class="abs search">
    <svg width="13" height="13" viewBox="0 0 13 13"><circle cx="5.5" cy="5.5" r="4" fill="none" stroke="#bbb" stroke-width="1.6"/><line x1="8.5" y1="8.5" x2="12" y2="12" stroke="#bbb" stroke-width="1.8"/></svg>
    Search
  </div>
  <nav class="abs main-nav">
    <a class="active" href="#">About Stitch Haven</a>
    <a href="#">Product</a>
    <a href="#">Shipping Info</a>
    <a href="#">Wholesale</a>
    <a href="#">Contact Us</a>
  </nav>
</header>
<div class="abs brand-tab">
  <span class="brand-dot"></span>
  <span class="brand-name">Stitch Haven</span>
</div>

<section class="abs hero">
  <div class="abs hero-image" role="img" aria-label="Close-up of pastel gingham ribbons in purple, pink, blue and yellow"></div>
  <svg class="abs hero-arrow" style="left:10px" width="14" height="30" viewBox="0 0 14 30"><polyline points="12,2 2,15 12,28" fill="none" stroke="#fff" stroke-width="3"/></svg>
  <svg class="abs hero-arrow" style="right:10px" width="14" height="30" viewBox="0 0 14 30"><polyline points="2,2 12,15 2,28" fill="none" stroke="#fff" stroke-width="3"/></svg>
</section>

<aside class="abs panel new-products">
  <div class="abs head"></div>
  <h2 class="panel-title">New Products</h2>
  <ul class="abs cat-list">
    <li>Adhesive</li><li>Buttons</li><li>Card Kits</li><li>Charms</li>
    <li>Clipboard</li><li>Adhesive</li><li>Buttons</li><li>Cards Kits</li>
  </ul>
</aside>

<section class="abs panel latest">
  <h2 class="panel-title">Latest Products</h2>
  <div class="abs card" style="left:8px;top:48px"><div class="thumb tape" role="img" aria-label="Blue patterned washi tape rolls"></div><div class="name">Washi Tape</div><div class="variant">Blue Pattern</div><div class="price">$3.50</div></div>
  <div class="abs card" style="left:110px;top:48px"><div class="thumb ribbon" role="img" aria-label="Brown pleated satin ribbon"></div><div class="name">Pleated Sated Ribbon</div><div class="variant">Brown</div><div class="price">$4.00</div></div>
  <div class="abs card" style="left:212px;top:48px"><div class="thumb tape" role="img" aria-label="Blue patterned washi tape rolls"></div><div class="name">Washi Tape</div><div class="variant">Blue Pattern</div><div class="price">$3.50</div></div>
  <div class="abs card" style="left:314px;top:48px"><div class="thumb ribbon" role="img" aria-label="Brown pleated satin ribbon"></div><div class="name">Pleated Sated Ribbon</div><div class="variant">Brown</div><div class="price">$4.00</div></div>
  <div class="abs card" style="left:416px;top:48px"><div class="thumb tape" role="img" aria-label="Blue patterned washi tape rolls"></div><div class="name">Washi Tape</div><div class="variant">Blue Pattern</div><div class="price">$3.50</div></div>
  <div class="abs card" style="left:8px;top:148px"><div class="thumb tape-mono" role="img" aria-label="Black and white bicycle print washi tape"></div><div class="name">Washi Tape</div><div class="variant">Bicylces</div><div class="price">$2.70</div></div>
  <div class="abs card" style="left:110px;top:148px"><div class="thumb button" role="img" aria-label="Black wooden buttons"></div><div class="name">Wodden Button</div><div class="variant">Medium Black</div><div class="price">$5.00</div></div>
</section>

<aside class="abs panel basket">
  <h2 class="panel-title">Shopping Basket</h2>
  <span class="panel-link">View Basket &nbsp;&gt;&gt;</span>
  <div class="abs basket-info">
    <p class="empty">Your Shopping Cart is empty</p>
    <p class="red">Items In Cart : 0</p>
    <p class="red">Total : $0.00</p>
  </div>
</aside>

<aside class="abs panel gallery">
  <h2 class="panel-title">Gallery</h2>
  <span class="panel-link">View All &gt;&gt;</span>
  <div class="abs card" style="left:9px;top:44px"><div class="thumb tape" role="img" aria-label="Blue patterned washi tape rolls"></div><div class="name">Washi Tape</div><div class="variant">Blue Pattern</div><div class="price">$3.50</div></div>
  <div class="abs card" style="left:112px;top:44px"><div class="thumb ribbon" role="img" aria-label="Brown pleated satin ribbon"></div><div class="name">Pleated Sated Ribbon</div><div class="variant">Brown</div><div class="price">$4.00</div></div>
</aside>

<section class="abs panel popular">
  <h2 class="panel-title">Popular Products</h2>
  <div class="abs deal" style="left:9px;top:46px"><p class="title">Inkwell Studio clear stamp - flourishes</p><p class="save">Save $16.95</p></div>
  <div class="abs deal" style="left:262px;top:46px"><p class="title">Inkwell Studio clear stamp - flourishes</p><p class="save">Save $12.50</p></div>
  <div class="abs deal" style="left:9px;top:86px"><p class="title">Inkwell Studio clear stamp - floral expressions</p><p class="save">Save $10.50</p></div>
  <div class="abs deal" style="left:262px;top:86px"><p class="title">Petal masks - 5 pieces 881993</p><p class="save">Save $7.95</p></div>
  <div class="abs deal" style="left:9px;top:127px"><p class="title">Marla Stone punch - pop up cosmos</p><p class="save">Save $7.00</p></div>
</section>

<aside class="abs panel subscribe">
  <h2 class="panel-title">Subscribe</h2>
  <p class="abs sub-note">Subscribe to our mailing list below:</p>
  <span class="abs sub-label">Email:</span>
  <div class="abs sub-input"></div>
  <span class="abs sub-btn">Join Now !</span>
</aside>

<h2 class="abs sales-title">Sales Item</h2>
<div class="abs deal" style="left:89px;top:840px"><p class="title">Inkwell Studio clear stamp - flourishes</p><p class="save">Save $16.95</p></div>
<div class="abs deal" style="left:352px;top:840px"><p class="title">Inkwell Studio clear stamp - flourishes</p><p class="save">Save $12.50</p></div>
<div class="abs deal" style="left:89px;top:876px"><p class="title">Inkwell Studio clear stamp - floral expressions</p><p class="save">Save $10.50</p></div>
<div class="abs deal" style="left:352px;top:876px"><p class="title">Petal masks - 5 pieces 881993</p><p class="save">Save $7.95</p></div>
<div class="abs deal" style="left:89px;top:912px"><p class="title">Marla Stone punch - pop up cosmos</p><p class="save">Save $7.00</p></div>

<aside class="abs panel join">
  <h2 class="panel-title">Join Us</h2>
  <span class="abs social-name" style="left:10px;top:55px">chatterbook</span>
  <span class="abs social-name" style="left:112px;top:55px">chirpline</span>
  <span class="abs social-name" style="left:10px;top:82px">snapboard</span>
</aside>

<section class="abs panel blogs">
  <h2 class="panel-title">Blogs</h2>
  <span class="abs quote-mark" style="left:26px;top:42px">&ldquo;</span>
  <p class="abs quote-text">I specialise in ribbons, buttons and unique craft materials. I sell online to individuals and shops with seperate retail and wholesale sites. The web page I'd like redesigned is my retail site.</p>
  <span class="abs quote-mark" style="right:24px;top:86px">&rdquo;</span>
  <span class="abs quote-by">-Admin</span>
</section>

<aside class="abs panel partners">
  <h2 class="panel-title">Our Partners</h2>
  <div class="abs badge" style="left:10px;top:48px;width:97px;height:48px"></div>
  <div class="abs badge" style="left:113px;top:48px;width:86px;height:32px;background:#3e3a78"></div>
</aside>

<section class="abs postage">
  <svg class="abs postage-flag" width="22" height="20" viewBox="0 0 22 20"><polygon points="0,0 22,0 22,20 11,12 0,20" fill="#e31b1b"/></svg>
  <div class="abs postage-text">
    <p>Postage rates (within Australia only)</p>
    <p>Orders over $50 - Free postage</p>
    <p>Orders under $50 - $6 postage charge</p>
    <p>NO international postage without prior postage price agreement. Please do not order online if you do not have an Australian address.</p>
  </div>
</section>

<footer class="abs footer">
  <div class="abs footer-links">About Stitch Haven<span>|</span>Contact Stitch Haven<span>|</span>Privacy Policy<span>|</span>Terms &amp; Conditions</div>
  <div class="abs footer-copy">All Right Reserved 2013-14 StitchHaven</div>
</footer>

</body>
</html>
```